National commercial insurance agency needs design for email campaign to other insurance agencies ...

National commercial insurance agency needs design for email campaign to other insurance agencies needing to place workers comp policies and and also need very intense risk management. We want to market to smaller insurance agencies to refer us to their larger clients or prospects.

Font styles to use
Sans Serif

```html
<!DOCTYPE html>
<html lang="en">
<head>
<meta charset="UTF-8">
<title>Riskbridge – The Answer When It Comes to Work Comp</title>
<link rel="stylesheet" href="https://fonts.googleapis.com/css2?family=Roboto:wght@400;500;700;900&display=swap">
<style>
:root{
  --orange:#f15a22;
  --dark:#2f2f2f;
  --ink:#222222;
  --text:#3a3a3a;
  --grey-band:#ececec;
  --white:#ffffff;
  --line:#d6d6d6;
}
*{margin:0;padding:0;box-sizing:border-box}
html,body{width:1200px;height:4748px;overflow:hidden;background:var(--white)}
body{font-family:"Roboto",Arial,sans-serif;color:var(--text);position:relative}
.abs{position:absolute}

/* hero */
.hero-accent{left:600px;top:0;width:600px;height:672px;background:var(--orange)}
.brand{left:100px;top:148px;width:370px;display:flex;align-items:center;gap:14px}
.brand-name{font-size:46px;font-weight:700;color:var(--dark);letter-spacing:1px;white-space:nowrap}
.brand-dot{flex:0 0 62px;width:62px;height:62px;border-radius:50%;background:var(--orange)}
.hero-title{left:100px;top:368px;font-size:80px;font-weight:900;line-height:1.0;color:var(--ink);letter-spacing:1px}
.hero-sub{left:100px;top:548px;font-size:32px;line-height:1.2;color:var(--ink);font-weight:500}
.hero-photo{left:500px;top:128px;width:500px;height:672px;background:linear-gradient(135deg,#c89466 0%,#e9d6bf 45%,#b47a4e 100%)}

/* mission */
.mission-title{left:0;top:872px;width:1200px;text-align:center;font-size:60px;font-weight:900;color:var(--ink)}
.mission-sub{left:300px;top:958px;width:600px;text-align:center;font-size:27px;font-weight:500;line-height:1.3;color:var(--ink);text-transform:uppercase}
.pillar{top:1160px;width:312px;height:540px;border:3px solid #cfcfcf;background:var(--white)}
.pillar-head{position:absolute;left:-3px;right:-3px;top:58px;height:110px;background:var(--dark);color:var(--white);font-size:30px;font-weight:700;display:flex;align-items:center;justify-content:center;letter-spacing:.5px}
.pillar-icon{position:absolute;left:50%;top:-82px;width:130px;height:130px;margin-left:-65px;border-radius:50%;background:var(--orange);display:flex;align-items:center;justify-content:center}
.pillar-body{position:absolute;left:26px;right:22px;top:196px;font-size:28px;line-height:1.3;color:var(--text)}

/* compliance */
.compliance-band{left:0;top:1780px;width:1200px;height:640px;background:var(--grey-band)}
.compliance-photo{left:100px;top:1848px;width:420px;height:672px;background:linear-gradient(135deg,#d6a06e 0%,#efe2d2 50%,#b98156 100%)}
.compliance-title{left:612px;top:1858px;font-size:52px;font-weight:900;line-height:1.04;color:var(--ink)}
.compliance-copy{left:612px;top:2062px;width:490px;font-size:27px;line-height:1.3;color:var(--text)}
.btn{left:612px;top:2268px;width:276px;height:76px;border-radius:38px;background:var(--orange);color:var(--white);font-size:26px;font-weight:500;display:flex;align-items:center;justify-content:center;gap:20px;text-decoration:none}

/* services */
.services-title{left:0;top:2622px;width:1200px;text-align:center;font-size:54px;font-weight:900;color:var(--ink)}
.service-list{left:100px;top:2834px;width:520px;list-style:none}
.service-list li{height:92px;display:flex;align-items:center;justify-content:space-between;font-size:31px;color:var(--ink);border-bottom:2px solid var(--line)}
.service-list li:last-child{border-bottom:none}
.services-photo{left:720px;top:2768px;width:420px;height:580px;background:linear-gradient(180deg,#8e9095 0%,#5d5f64 60%,#3a3b3f 100%)}

/* experience mod */
.mod-band{left:0;top:3688px;width:1200px;height:872px;background:var(--grey-band)}
.mod-photo{left:220px;top:3480px;width:760px;height:580px;background:linear-gradient(135deg,#6d8fb5 0%,#d9d4cc 40%,#8c9aa6 70%,#e0b640 100%)}
.mod-title{left:0;top:4140px;width:1200px;text-align:center;font-size:52px;font-weight:900;line-height:1.05;color:var(--ink)}
.mod-copy{left:200px;top:4290px;width:800px;text-align:center;font-size:27px;line-height:1.3;color:var(--text)}

/* footer */
.footer{left:0;top:4560px;width:1200px;height:188px;background:var(--orange);color:var(--white);font-size:27px;text-align:center;line-height:1.55;display:flex;flex-direction:column;justify-content:center}
</style>
</head>
<body>

<div class="abs hero-accent"></div>
<div class="abs hero-photo" role="img" aria-label="Hands joining two puzzle pieces together"></div>
<div class="abs brand"><span class="brand-name">RISKBRIDGE</span><span class="brand-dot"></span></div>
<h1 class="abs hero-title">THE<br>ANSWER</h1>
<p class="abs hero-sub">WHEN IT COMES<br>TO WORK COMP</p>

<h2 class="abs mission-title">OUR MISSION</h2>
<p class="abs mission-sub">Is to reduce employers' workers' compensation costs</p>

<section class="abs pillar" style="left:100px">
  <div class="pillar-icon">
    <svg width="64" height="64" viewBox="0 0 64 64" fill="none" stroke="#fff" stroke-width="4" stroke-linejoin="round"><path d="M24 8h16v22H24z"/><path d="M10 36h44v12H10z"/><path d="M14 56h36"/></svg>
  </div>
  <div class="pillar-head">COMPLIANCE</div>
  <p class="pillar-body">HR and Safety onsite compliance audits are available, as well as training and certification for all types of businesses.</p>
</section>
<section class="abs pillar" style="left:444px">
  <div class="pillar-icon">
    <svg width="66" height="64" viewBox="0 0 66 64" fill="none" stroke="#fff" stroke-width="4" stroke-linejoin="round"><rect x="6" y="14" width="54" height="34" rx="4"/><circle cx="33" cy="31" r="8"/><path d="M14 22v18M52 22v18"/></svg>
  </div>
  <div class="pillar-head">PROFIT LEAKS</div>
  <p class="pillar-body">We detect and correct the profit leaks inherent in every work comp program that drives the costs.</p>
</section>
<section class="abs pillar" style="left:788px">
  <div class="pillar-icon">
    <svg width="60" height="64" viewBox="0 0 60 64" fill="none" stroke="#fff" stroke-width="4" stroke-linejoin="round"><path d="M10 6h28l12 12v40H10z"/><path d="M38 6v12h12"/><path d="M18 32h24M18 42h24M18 50h14"/></svg>
  </div>
  <div class="pillar-head">CLAIMS</div>
  <p class="pillar-body">We provide employers with immediate, ongoing injury and claims management consulting.</p>
</section>

<div class="abs compliance-band"></div>
<div class="abs compliance-photo" role="img" aria-label="Hands fitting puzzle pieces together"></div>
<h2 class="abs compliance-title">IS YOUR<br>COMPANY IN<br>COMPLIANCE?</h2>
<p class="abs compliance-copy">Riskbridge offers HR and Safety onsite compliance audits, as well as training and certification for all types of businesses.</p>
<a class="abs btn" href="#">Learn More
  <svg width="14" height="22" viewBox="0 0 14 22" fill="none" stroke="#fff" stroke-width="3"><path d="M3 3l8 8-8 8"/></svg>
</a>

<h2 class="abs services-title">OUR SERVICES</h2>
<ul class="abs service-list">
  <li>HR Services<svg width="14" height="22" viewBox="0 0 14 22" fill="none" stroke="#444" stroke-width="3"><path d="M3 3l8 8-8 8"/></svg></li>
  <li>Safety Compliance Training<svg width="14" height="22" viewBox="0 0 14 22" fill="none" stroke="#444" stroke-width="3"><path d="M3 3l8 8-8 8"/></svg></li>
  <li>Employee Safety<svg width="14" height="22" viewBox="0 0 14 22" fill="none" stroke="#444" stroke-width="3"><path d="M3 3l8 8-8 8"/></svg></li>
  <li>Re-Audit Services<svg width="14" height="22" viewBox="0 0 14 22" fill="none" stroke="#444" stroke-width="3"><path d="M3 3l8 8-8 8"/></svg></li>
  <li>Premium Recovery Services<svg width="14" height="22" viewBox="0 0 14 22" fill="none" stroke="#444" stroke-width="3"><path d="M3 3l8 8-8 8"/></svg></li>
</ul>
<div class="abs services-photo" role="img" aria-label="Businesswoman in a dark suit standing with arms crossed"></div>

<div class="abs mod-band"></div>
<div class="abs mod-photo" role="img" aria-label="Collage of workers in factories, workshops and warehouses"></div>
<h2 class="abs mod-title">IS YOUR EXPERIENCE<br>MOD CORRECT?</h2>
<p class="abs mod-copy">Our CSP (Certified Safety Professional) can provide written programs and onsite training for Blood Borne Pathogens, DOT, OSHA 10 &amp; 30, Roadway Flagger Certification, Forklift, CPR/First Aid, and Ergonomics just to name a few.</p>

<footer class="abs footer">
  <div>48 Harlow Ave. Suite 5, Cedarville, FL 33012</div>
  <div>info@riskbridge.com &nbsp;|&nbsp; 555.014.2290 &nbsp;|&nbsp; riskbridge.com</div>
</footer>

</body>
</html>
```